Motor Mate 4x6 Flyer

Need 4 x 6 Flyer with following language:

Willow Crest Motor Mate
Our Motor Mate Will Come to Your Home
Our Motor Mate will Drive Your Car to Nearest Gas Station
Our Motor Mate will Fill-up Your Car with Gas
Our Motor Mate will Immediately Return Your Car
Your Car Covered with $100k of Commercial Insurance
Member Dunmore Chamber of Commerce / Honest Merchant League
www.willowcrestmotormate.example

Place logos of Vortan, Brenn & Dorvane on Left Side of Flyer starting at top left corner, mid left side, left bottom corner.
Place logos of BoltNest, 12-Forty, Tesmira on opposite side right.....
Place Willow Crest Motor Mate Logo on both sides of very top that says Willow Crest Motor Mate

Target Market(s)

Upscale Home Owners

Font styles to use
Sans Serif

Colors
F0912C
F2A743
F7CA91
FBE8D2
FDF5EE

Requirements
Must have
• Flyer Must be Bright Orange

```html
<!DOCTYPE html>
<html lang="en">
<head>
<meta charset="utf-8">
<title>Willow Crest Motor Mate – 4x6 Flyer</title>
<link href="https://fonts.googleapis.com/css2?family=Roboto:wght@500&family=Roboto+Condensed:wght@400;700&display=swap" rel="stylesheet">
<style>
  :root {
    --orange-deep: #F0912C;
    --orange: #F2A743;
    --peach: #F7CA91;
    --cream: #FBE8D2;
    --ivory: #FDF5EE;
    --backdrop: #EBE8E6;
    --ink: #1C1C1C;
    --mark-red: #E2322B;
    --white: #FFFFFF;
  }
  * { box-sizing: border-box; margin: 0; padding: 0; }
  html, body { width: 1200px; height: 857px; overflow: hidden; }
  body {
    background: var(--backdrop);
    position: relative;
    font-family: "Roboto Condensed", sans-serif;
    color: var(--ink);
  }
  .flyer {
    position: absolute;
    top: 106px;
    height: 645px;
    display: flex;
  }
  .flyer--front { left: 117px; width: 439px; }
  .flyer--back { left: 645px; width: 438px; }

  .brand-rail {
    height: 100%;
    background: linear-gradient(180deg, var(--peach) 0%, var(--cream) 45%, var(--ivory) 100%);
    position: relative;
  }
  .flyer--front .brand-rail { width: 135px; }
  .flyer--back .brand-rail { width: 146px; }

  .rail-item {
    position: absolute;
    left: 0; right: 0;
    transform: translateY(-50%);
    display: flex;
    justify-content: center;
    align-items: center;
  }
  .partner-name {
    font-family: "Roboto Condensed", sans-serif;
    font-weight: 700;
    font-size: 22px;
    color: var(--mark-red);
  }
  .partner-dot {
    width: 12px; height: 12px;
    border-radius: 50%;
    background: var(--mark-red);
    margin-right: 6px;
  }
  .rail-art {
    width: 70px; height: 78px;
    border-radius: 6px;
    opacity: .9;
  }
  .rail-art--rig { background: linear-gradient(180deg, #F4B06A, #D9A57A); }
  .rail-art--wind { background: linear-gradient(180deg, #E7E3DC, #CFD5BE); }

  .panel {
    flex: 1;
    display: flex;
    flex-direction: column;
  }
  .panel-head {
    height: 165px;
    background: var(--white);
    display: flex;
    flex-direction: column;
    align-items: center;
    justify-content: flex-end;
    padding-bottom: 40px;
  }
  .head-mark {
    width: 40px; height: 40px;
    background: var(--mark-red);
    border-radius: 4px;
    margin-bottom: 14px;
  }
  .head-name {
    font-family: "Roboto", sans-serif;
    font-weight: 500;
    font-size: 16px;
  }
  .panel-body {
    flex: 1;
    position: relative;
    padding: 28px 0 0 16px;
    background:
      radial-gradient(ellipse 60% 45% at 70% 20%, rgba(253,245,238,.55), transparent 70%),
      radial-gradient(ellipse 55% 40% at 30% 85%, rgba(247,202,145,.6), transparent 70%),
      linear-gradient(180deg, var(--peach) 0%, var(--orange) 55%, var(--orange-deep) 100%);
  }
  .headline {
    font-weight: 700;
    font-size: 29px;
    line-height: 1;
    letter-spacing: -.2px;
    margin-bottom: 18px;
  }
  .benefit {
    font-size: 20px;
    line-height: 24px;
    margin-bottom: 20px;
  }
  .benefit--small {
    font-size: 17px;
    line-height: 21px;
  }
  .site {
    font-size: 16px;
    margin-top: 2px;
  }
  .tools-art {
    position: absolute;
    left: 18px;
    bottom: 33px;
    width: 260px;
    height: 106px;
    border-radius: 6px;
    background: linear-gradient(90deg, #D8362C 0%, #E9B233 45%, #2F3C7E 58%, #D8362C 100%);
    opacity: .85;
  }
</style>
</head>
<body>

  <section class="flyer flyer--front">
    <aside class="brand-rail">
      <div class="rail-item" style="top:78px"><span class="partner-name">Vortan</span></div>
      <div class="rail-item" style="top:185px"><div class="rail-art rail-art--rig" role="img" aria-label="Illustration of an oil rig with a gas flare and storage tank"></div></div>
      <div class="rail-item" style="top:322px"><span class="partner-dot"></span><span class="partner-name">Brenn</span></div>
      <div class="rail-item" style="top:438px"><div class="rail-art rail-art--wind" role="img" aria-label="Illustration of wind turbines on a hill"></div></div>
      <div class="rail-item" style="top:549px"><span class="partner-name">Dorvane</span></div>
    </aside>
    <main class="panel">
      <header class="panel-head">
        <div class="head-mark"></div>
        <div class="head-name">Willow Crest Motor Mate</div>
      </header>
      <div class="panel-body">
        <h1 class="headline">Willow Crest Motor Mate</h1>
        <p class="benefit">Our Motor Mate Will Come<br>to Your Home</p>
        <p class="benefit">Our Motor Mate will Drive<br>Your Car to Nearest Gas Station</p>
        <p class="benefit">Our Motor Mate will Fill-up<br>Your Car with Gas</p>
        <p class="site">www.willowcrestmotormate.example</p>
        <div class="tools-art" role="img" aria-label="Illustration of a fuel canister, light bulb, batteries and a gas pump"></div>
      </div>
    </main>
  </section>

  <section class="flyer flyer--back">
    <main class="panel">
      <header class="panel-head">
        <div class="head-mark"></div>
        <div class="head-name">Willow Crest Motor Mate</div>
      </header>
      <div class="panel-body">
        <h1 class="headline">Willow Crest Motor Mate</h1>
        <p class="benefit">Our Motor Mate will Immediately<br>Return Your Car</p>
        <p class="benefit">Your Car Covered with $100k<br>of Commercial Insurance</p>
        <p class="benefit benefit--small">Member Dunmore Chamber of<br>Commerce / Honest Merchant League</p>
        <p class="site">www.willowcrestmotormate.example</p>
        <div class="tools-art" role="img" aria-label="Illustration of a fuel canister, light bulb, batteries and a gas pump"></div>
      </div>
    </main>
    <aside class="brand-rail">
      <div class="rail-item" style="top:82px"><span class="partner-name">BoltNest</span></div>
      <div class="rail-item" style="top:185px"><div class="rail-art rail-art--rig" role="img" aria-label="Illustration of an oil rig with a gas flare and storage tank"></div></div>
      <div class="rail-item" style="top:322px"><span class="partner-name">12-Forty</span></div>
      <div class="rail-item" style="top:438px"><div class="rail-art rail-art--wind" role="img" aria-label="Illustration of wind turbines on a hill"></div></div>
      <div class="rail-item" style="top:558px"><span class="partner-name">Tesmira</span></div>
    </aside>
  </section>

</body>
</html>
```